Graphic design for Student Conference

We need design work done for our annual student conference called Lantern Fest. We have a central logo but need design work done to use on posters, banners, etc. that tie into the theme for this year's conference. The theme is "Be Glad" and I would like the design elements to have a very fun, 1980's or 1990's vibe to them. The feeling of happiness and joy should be felt in the design.

Target Market(s)

Students 10-12 years of age

Industry/Entity Type

Church

Requirements
Must have
• Must include the Lantern Fest logo - event date: June 19-21 - event website: brightoakparish.org/lanternfest - Flexible supporting artwork elements that can be used in a variety of mediums. - Must use fonts that are available from free, open sources or can be provided upon delivery of completed project.
Should not have
• Anything crude, scary or content inappropriate for middle school students. Should not have any imagery related to a classroom or meeting.

```html
<!DOCTYPE html>
<html lang="en">
<head>
<meta charset="utf-8">
<title>Be Glad – Lantern Fest</title>
<link rel="stylesheet" href="https://fonts.googleapis.com/css2?family=Bowlby+One&family=Montserrat:wght@900&family=Red+Hat+Display:wght@700;800;900&display=swap">
<style>
  :root {
    --bg-violet: #c2aefc;
    --bg-blue: #7fb4fb;
    --bg-green: #c6fca6;
    --bg-pink: #ff9edf;
    --panel: #5470d8;
    --headline: #f512c8;
    --headline-shadow: #394c93;
    --event-name: #ffe825;
    --date: #c6f98a;
    --url: #fdf2ea;
  }
  * { margin: 0; padding: 0; box-sizing: border-box; }
  html, body { width: 1200px; height: 1200px; overflow: hidden; }
  body {
    position: relative;
    background:
      radial-gradient(circle at 100% 0%, var(--bg-blue) 0%, transparent 45%),
      radial-gradient(circle at 0% 100%, var(--bg-green) 0%, transparent 60%),
      radial-gradient(circle at 100% 100%, var(--bg-pink) 0%, transparent 65%),
      var(--bg-violet);
  }
  .panel {
    position: absolute;
    left: 92px; top: 181px;
    width: 1016px; height: 865px;
    background: var(--panel);
    border-radius: 40px;
  }
  .headline {
    position: absolute;
    left: 140px; top: 120px;
    width: 960px; height: 260px;
  }
  .event-name {
    position: absolute;
    left: 92px; width: 1016px; top: 470px;
    text-align: center;
    font-family: "Montserrat", sans-serif;
    font-weight: 900;
    font-size: 88px;
    line-height: 1;
    color: var(--event-name);
  }
  .event-date {
    position: absolute;
    left: 92px; width: 1016px; top: 672px;
    text-align: center;
    font-family: "Red Hat Display", sans-serif;
    font-weight: 900;
    font-size: 128px;
    line-height: 1;
    letter-spacing: -3px;
    color: var(--date);
  }
  .event-url {
    position: absolute;
    left: 92px; width: 1016px; top: 828px;
    text-align: center;
    font-family: "Red Hat Display", sans-serif;
    font-weight: 800;
    font-size: 55px;
    line-height: 1;
    color: var(--url);
  }
  .floats-art {
    position: absolute;
    left: 328px; top: 928px;
    width: 543px; height: 165px;
    border-radius: 60px;
    background: linear-gradient(120deg, #4fd6ff 0%, #b67cff 40%, #ff6a8a 70%, #5ff0ff 100%);
    opacity: 0.85;
  }
</style>
</head>
<body>
  <div class="panel"></div>

  <svg class="headline" viewBox="0 0 960 260" role="img" aria-label="Be Glad">
    <g font-family="'Bowlby One', sans-serif" font-size="236" text-anchor="middle">
      <text x="488" y="234" textLength="920" lengthAdjust="spacingAndGlyphs" fill="var(--headline-shadow)">BE GLAD</text>
      <text x="478" y="224" textLength="920" lengthAdjust="spacingAndGlyphs" fill="var(--headline)">BE GLAD</text>
    </g>
  </svg>

  <p class="event-name">LANTERN FEST</p>
  <p class="event-date">JUNE 19–21</p>
  <p class="event-url">brightoakparish.org/lanternfest</p>

  <div class="floats-art" role="img" aria-label="Three iridescent inflatable flamingo pool floats in a row"></div>
</body>
</html>
```